Foldable Bluetooth Headphone Packaging Design

We would like a window box style packaging design for our Foldable Bluetooth Headphone.

We want to use the packaging for 4-5 of our Bluetooth headphone series (enclosed picture of the headphones for reference) and hence we would not like to put any product pictures on the packaging.
Material: E-Flute Paper box
Type: Window Box style
Design features we prefer: Colorful, creative, trendy, High tech.
Requirement: AI file is preferred
Size of Packaging: 170 (L) x 120 (W) x 200 (H) mm

Enclosed are a detailed description along with competitor designs for your reference.

Any further questions, please feel free to ask.

Target Market(s)

25-35 year olds

Industry/Entity Type

Electronics

Colors

Designer to choose colors to be used in the design.

Requirements
Must have
• Trendy Design

```html
<!DOCTYPE html>
<html lang="en">
<head>
<meta charset="utf-8">
<title>Foldable Bluetooth Headphone – Box Dieline</title>
<link rel="stylesheet" href="https://fonts.googleapis.com/css2?family=Oswald:wght@300&family=Roboto+Condensed:wght@700;800&family=Open+Sans:wght@400&display=swap">
<style>
  :root {
    --paper: #f2f2f4;
    --white: #ffffff;
    --navy: #2e3192;
    --red: #ed1c24;
    --yellow: #fff200;
    --sky: #25a9e0;
    --cyan: #00aeef;
    --grey-ring: #939598;
    --orange: #f7941d;
    --ink: #111111;
    --edge: #333333;
  }
  html, body {
    margin: 0;
    padding: 0;
    width: 1200px;
    height: 1200px;
    overflow: hidden;
    background: var(--white);
  }
  .dieline { display: block; width: 1200px; height: 1200px; }
  .panel-edge { fill: none; stroke: var(--edge); stroke-width: 1; }
  .fill-paper { fill: var(--paper); }
  .fill-red { fill: var(--red); }
  .fill-yellow { fill: var(--yellow); }
  .fill-sky { fill: var(--sky); }
  .fill-cyan { fill: var(--cyan); }
  .fill-navy { fill: var(--navy); }
  .ring-navy { fill: none; stroke: var(--navy); stroke-width: 30; }
  .ring-grey { fill: none; stroke: var(--grey-ring); stroke-width: 30; }
  .handle { fill: none; stroke: var(--navy); stroke-width: 25; }
  .tagline {
    font-family: "Oswald", sans-serif;
    font-weight: 300;
  }
  .product-name {
    font-family: "Roboto Condensed", sans-serif;
    font-weight: 800;
  }
  .tagline--navy, .product-name--navy { fill: var(--navy); }
  .tagline--white { fill: var(--white); }
  .tagline--red, .product-name--red { fill: var(--red); }
  .product-name--ink { fill: var(--ink); }
  .small-copy {
    font-family: "Open Sans", sans-serif;
    font-size: 11px;
    fill: var(--ink);
  }
  .spec-copy {
    font-family: "Open Sans", sans-serif;
    font-size: 12px;
    fill: var(--ink);
  }
</style>
</head>
<body>
<svg class="dieline" viewBox="0 0 1500 1500" xmlns="http://www.w3.org/2000/svg">
  <defs>
    <linearGradient id="photo-tone" x1="0" y1="0" x2="1" y2="1">
      <stop offset="0" stop-color="#ffffff"/>
      <stop offset="0.6" stop-color="#e4e4e6"/>
      <stop offset="1" stop-color="#bdbdc0"/>
    </linearGradient>
    <linearGradient id="dark-photo-tone" x1="0" y1="0" x2="1" y2="1">
      <stop offset="0" stop-color="#3a3a3a"/>
      <stop offset="1" stop-color="#9a9a9c"/>
    </linearGradient>
    <linearGradient id="name-band" x1="0" y1="0" x2="1" y2="0">
      <stop offset="0" stop-color="var(--orange)"/>
      <stop offset="0.45" stop-color="var(--orange)"/>
      <stop offset="0.6" stop-color="#b5d334"/>
      <stop offset="1" stop-color="#7fd3f0"/>
    </linearGradient>
    <clipPath id="window-front"><ellipse cx="353" cy="718" rx="160" ry="234"/></clipPath>
    <clipPath id="window-back"><ellipse cx="1175" cy="718" rx="160" ry="234"/></clipPath>
    <clipPath id="half-left-front"><rect x="100" y="400" width="253" height="640"/></clipPath>
    <clipPath id="half-right-front"><rect x="353" y="400" width="260" height="640"/></clipPath>
    <clipPath id="half-left-back"><rect x="920" y="400" width="255" height="640"/></clipPath>
    <clipPath id="half-right-back"><rect x="1175" y="400" width="260" height="640"/></clipPath>
    <clipPath id="above-back"><rect x="900" y="300" width="560" height="135"/></clipPath>
  </defs>

  <!-- Top flap -->
  <g class="flap flap--top">
    <rect class="fill-paper" x="112" y="95" width="482" height="340"/>
    <rect class="fill-navy" x="338" y="95" width="30" height="340"/>
    <text class="tagline tagline--navy" font-size="30" transform="translate(306 390) rotate(-90)" textLength="225" lengthAdjust="spacingAndGlyphs">FOLDABLE BLUETOOTH</text>
    <text class="product-name product-name--navy" font-size="40" transform="translate(339 390) rotate(-90)" textLength="225" lengthAdjust="spacingAndGlyphs">HEADPHONE</text>
    <path role="img" aria-label="Product photo: folded headphone, side view" fill="url(#dark-photo-tone)" d="M594 120 C520 140 470 210 478 290 C485 340 510 380 530 392 L560 300 C545 250 555 190 594 170 Z"/>
    <rect class="panel-edge" x="112" y="95" width="482" height="340"/>
  </g>

  <!-- Front panel -->
  <g class="panel panel--front">
    <rect class="fill-yellow" x="112" y="435" width="226" height="283"/>
    <rect class="fill-red" x="338" y="435" width="256" height="283"/>
    <rect class="fill-red" x="112" y="718" width="226" height="284"/>
    <rect class="fill-yellow" x="338" y="718" width="256" height="284"/>
    <g clip-path="url(#window-front)">
      <rect role="img" aria-label="Window showing the headphone" fill="url(#photo-tone)" x="190" y="480" width="163" height="238"/>
      <rect class="fill-sky" x="353" y="480" width="200" height="238"/>
      <rect class="fill-cyan" x="190" y="718" width="163" height="240"/>
      <rect role="img" aria-label="Window showing the headphone" fill="url(#photo-tone)" x="353" y="718" width="200" height="240"/>
    </g>
    <ellipse class="ring-navy" cx="353" cy="718" rx="180" ry="250" clip-path="url(#half-left-front)"/>
    <ellipse class="ring-grey" cx="353" cy="718" rx="180" ry="250" clip-path="url(#half-right-front)"/>
    <rect class="fill-navy" x="338" y="435" width="30" height="567"/>

    <text class="tagline tagline--white" font-size="30" x="112" y="746" textLength="226" lengthAdjust="spacingAndGlyphs">FOLDABLE BLUETOOTH</text>

    <g class="feature-list">
      <text class="small-copy" x="370" y="646">• Bluetooth V5</text>
      <text class="small-copy" x="370" y="655">• Foldable and Portable</text>
      <text class="small-copy" x="370" y="664">• Exceptional Sound Quality</text>
      <text class="small-copy" x="370" y="674">• Dual Mode wireless or wired connectivity</text>
      <text class="small-copy" x="370" y="683">• Adjustable headband</text>
    </g>
    <rect fill="url(#name-band)" x="368" y="686" width="226" height="32"/>
    <text class="product-name product-name--ink" font-size="36" x="370" y="716" textLength="223" lengthAdjust="spacingAndGlyphs">HEADPHONE</text>
  </g>

  <!-- Side panel -->
  <g class="panel panel--side">
    <rect class="fill-paper" x="594" y="435" width="340" height="283"/>
    <rect class="fill-red" x="594" y="718" width="340" height="284"/>
    <path role="img" aria-label="Product photo: folded headphone, top view" fill="url(#dark-photo-tone)" d="M632 435 L900 435 L900 500 C860 540 800 555 760 552 C700 550 650 510 632 435 Z"/>
    <text class="tagline tagline--red" font-size="30" x="650" y="692" textLength="223" lengthAdjust="spacingAndGlyphs">FOLDABLE BLUETOOTH</text>
    <text class="product-name product-name--red" font-size="36" x="650" y="720" textLength="223" lengthAdjust="spacingAndGlyphs">HEADPHONE</text>
    <rect class="panel-edge" x="594" y="435" width="340" height="567"/>
  </g>

  <!-- Back panel -->
  <g class="panel panel--back">
    <circle class="handle" cx="1175" cy="560" r="190" clip-path="url(#above-back)"/>
    <rect class="fill-red" x="934" y="435" width="226" height="283"/>
    <rect class="fill-yellow" x="1160" y="435" width="256" height="283"/>
    <rect class="fill-yellow" x="934" y="718" width="226" height="284"/>
    <rect class="fill-red" x="1160" y="718" width="256" height="284"/>
    <g clip-path="url(#window-back)">
      <rect class="fill-sky" x="1010" y="480" width="165" height="238"/>
      <rect role="img" aria-label="Window showing the headphone" fill="url(#photo-tone)" x="1175" y="480" width="165" height="238"/>
      <rect role="img" aria-label="Window showing the headphone" fill="url(#photo-tone)" x="1010" y="718" width="165" height="240"/>
      <rect class="fill-cyan" x="1175" y="718" width="165" height="240"/>
    </g>
    <ellipse class="ring-grey" cx="1175" cy="718" rx="180" ry="250" clip-path="url(#half-left-back)"/>
    <ellipse class="ring-navy" cx="1175" cy="718" rx="180" ry="250" clip-path="url(#half-right-back)"/>
    <rect class="fill-navy" x="1160" y="435" width="30" height="567"/>

    <g class="spec-list">
      <text class="spec-copy" x="1193" y="735">Specification:</text>
      <text class="spec-copy" x="1193" y="747">Bluetooth Version: 5.0</text>
      <text class="spec-copy" x="1193" y="759">Wireless Playback Duration: 10-12 h</text>
      <text class="spec-copy" x="1193" y="771">Standby Time: 80 h</text>
      <text class="spec-copy" x="1193" y="784">Wireless Range: 10 m</text>
      <text class="spec-copy" x="1193" y="796">Impedance: 32 Ω</text>
      <text class="spec-copy" x="1193" y="808">Sound Pressure Level: 100dB ± 3dB</text>
      <text class="spec-copy" x="1193" y="820">Frequency Response: 20-20kHz</text>
      <text class="spec-copy" x="1193" y="832">Plug Type: 3.5mm Stereo Detachable</text>
      <text class="spec-copy" x="1193" y="844">Driver Unit: 40mm</text>
    </g>
  </g>

  <!-- Bottom flap -->
  <g class="flap flap--bottom">
    <rect class="fill-paper" x="112" y="1002" width="482" height="340"/>
    <rect class="fill-navy" x="338" y="1002" width="30" height="340"/>
    <text class="tagline tagline--navy" font-size="30" transform="translate(306 1293) rotate(-90)" textLength="225" lengthAdjust="spacingAndGlyphs">FOLDABLE BLUETOOTH</text>
    <text class="product-name product-name--navy" font-size="40" transform="translate(339 1293) rotate(-90)" textLength="225" lengthAdjust="spacingAndGlyphs">HEADPHONE</text>
    <path role="img" aria-label="Product photo: folded headphone, side view" fill="url(#dark-photo-tone)" d="M112 1305 C180 1290 230 1220 230 1160 C230 1110 205 1060 175 1040 L150 1130 C160 1180 150 1240 112 1260 Z"/>
    <rect class="panel-edge" x="112" y="1002" width="482" height="340"/>
  </g>
</svg>
</body>
</html>
```